Advertising flyer for proofreading business.

Hello everyone,

I need an advertising flyer for a new proofreading company in Australia.

I would like your design in be in two sizes:
- A4 (to be posted on noticeboards),
- A6 (to be printed in larger quantity to give away)
(please see the size specification file attached).

The text file is attached (Ad Text) and it contains lots of information. Please feel free to include your choice of text from the text file, but please include Poster title, and highlight 'ESL' and students discounts.

I understand that it is impossible to include the same amount of information on A6 and A4, so please feel free to chose what fits on each of them, but please keep the design similar.

I have attached our company logo, but feel free to adjust it to the poster design (feel free to change the color as well). The original logo file contains circle around it, please feel free to remove it and include only the typeset as it can be seen here: http://www.vellumcheck.com.au/.

Flyers will be printed, so please see the specification file for details.

I will do my best to respond to feedback as soon as possible.

I appreciate your participation, time and help,
Best wishes,
Radoslaw

Target Market(s)

Students, authors

Industry/Entity Type

Business

Colors

Designer to choose colors to be used in the design.

Requirements
Must have
• It would be good if poster is easy to spot on busy noticeboards and attract attention.
• Please keep the poster in the positive/optimistic mood, and so that it focuses on students, maybe photos of graduates(?).
• Poster title,
• Please include the list of proof-read documents as they are described in the attached text file (Ad Text).
• Please highlight students discounts and ESL.
Nice to have
• I would like to leave the creative freedom to all designers so at this point I have not adjusted the Look and Feel sliders. Please feel free to offer your own take on this.
• It would be nice if most of the text could be fit to the poster.

```html
<!DOCTYPE html>
<html lang="en">
<head>
<meta charset="utf-8">
<title>VellumCheck – Professional Proofreading Services Flyer</title>
<link rel="stylesheet" href="https://fonts.googleapis.com/css2?family=Arimo:wght@400;700&family=Tinos:wght@400;700&display=swap">
<style>
  :root {
    --teal: #22bfa0;
    --ink: #222222;
    --slate: #5e5e5e;
    --paper: #ffffff;
    --backdrop: #2a2a2a;
    --sans: "Arimo", Arial, sans-serif;
    --serif: "Tinos", "Times New Roman", serif;
  }
  * { margin: 0; padding: 0; box-sizing: border-box; }
  html, body { width: 1200px; height: 850px; overflow: hidden; }
  body { background: var(--backdrop); position: relative; font-family: var(--serif); }

  .flyer {
    position: absolute;
    width: 475px; height: 672px;
    background: var(--paper);
    overflow: hidden;
    box-shadow: 0 6px 18px rgba(0,0,0,.45);
  }
  .flyer--a4 { left: 180px; top: 88px; }
  .flyer--a6 { left: 725px; top: 215px; transform: scale(0.621); transform-origin: top left; }

  .flyer__shapes { position: absolute; inset: 0; }

  .brand-mark {
    position: absolute; left: 312px; top: 46px; width: 160px;
    font-family: var(--sans); font-size: 24px; color: var(--paper);
    text-align: center; white-space: nowrap;
  }

  .title { position: absolute; left: 20px; top: 52px; font-family: var(--sans); }
  .title__name { font-size: 33px; font-weight: 700; color: var(--paper); letter-spacing: -0.6px; line-height: 1; white-space: nowrap; }
  .title__tagline { font-size: 16.5px; color: var(--paper); margin-top: 5px; letter-spacing: 0.1px; }
  .title__services { font-size: 55px; color: var(--ink); line-height: 1; margin-top: 2px; letter-spacing: -0.5px; }

  .details { position: absolute; left: 188px; top: 230px; width: 272px; }
  .details__heading {
    font-size: 13px; font-weight: 700; color: var(--teal); line-height: 14px;
    display: flex; align-items: center; gap: 5px; margin-bottom: 6px; white-space: nowrap;
  }
  .details__heading svg { width: 14px; height: 13px; flex: none; }
  .details__list { list-style: none; margin: 0 0 7px 18px; }
  .details__list li {
    position: relative; font-size: 9.4px; line-height: 10px; color: var(--ink);
    padding-left: 16px; margin-bottom: 6px;
  }
  .details__list li::before {
    content: ""; position: absolute; left: 2px; top: 3px;
    width: 4px; height: 4px; border-radius: 50%; background: var(--ink);
  }
  .details__list--docs li { margin-bottom: 7.5px; }

  .testimonial { position: absolute; left: 13px; top: 384px; width: 136px; color: var(--paper); }
  .testimonial__label { font-size: 20px; font-weight: 700; margin-bottom: 12px; }
  .testimonial__quote { font-size: 12px; line-height: 14.5px; text-align: justify; position: relative; padding-top: 14px; }
  .testimonial__quote .mark { font-size: 24px; font-weight: 700; line-height: 0; position: relative; top: 8px; }
  .testimonial__quote .mark--open { position: absolute; left: 0; top: 10px; }
  .testimonial__author { margin: 24px 0 0 54px; width: 160px; }
  .testimonial__name { font-size: 17px; font-weight: 700; }
  .testimonial__role { font-size: 9.5px; font-weight: 700; line-height: 11px; }

  .website { position: absolute; left: 18px; top: 637px; font-size: 16.5px; font-weight: 700; color: var(--paper); }

  .contact { position: absolute; left: 222px; top: 586px; width: 250px; }
  .contact__cta { font-size: 12.5px; font-weight: 700; color: var(--teal); white-space: nowrap; }
  .contact__phone { font-size: 40px; font-weight: 700; color: var(--teal); line-height: 1; margin-top: 1px; letter-spacing: 0.3px; white-space: nowrap; }
  .contact__email { display: flex; align-items: center; gap: 5px; margin: 5px 0 0 16px; font-size: 13.5px; color: var(--ink); }
  .contact__email svg { width: 12px; height: 12px; flex: none; }

  .size-label { position: absolute; font-family: var(--sans); font-weight: 700; font-size: 34px; color: var(--paper); }
  .size-label--a4 { left: 390px; top: 782px; }
  .size-label--a6 { left: 845px; top: 655px; }
</style>
</head>
<body>

<svg width="0" height="0" style="position:absolute">
  <defs>
    <symbol id="icon-tick" viewBox="0 0 14 13"><path d="M1 7 L5 11 L13 1" fill="none" stroke="#22bfa0" stroke-width="2.2" stroke-linecap="round" stroke-linejoin="round"/></symbol>
    <symbol id="icon-mail" viewBox="0 0 12 12"><circle cx="6" cy="6" r="5.5" fill="#222"/><rect x="3" y="4" width="6" height="4.2" fill="#fff"/><path d="M3 4 L6 6.4 L9 4" fill="none" stroke="#222" stroke-width="0.8"/></symbol>
  </defs>
</svg>

<!-- A4 flyer -->
<article class="flyer flyer--a4">
  <svg class="flyer__shapes" viewBox="0 0 475 672" aria-hidden="true">
    <polygon points="0,0 475,0 475,127 0,282" fill="var(--teal)"/>
    <polygon points="0,282 105,248 212,672 0,672" fill="var(--slate)"/>
    <circle cx="390" cy="32" r="95" fill="var(--ink)"/>
  </svg>
  <div class="brand-mark">VellumCheck</div>
  <header class="title">
    <div class="title__name">VELLUMCHECK</div>
    <div class="title__tagline">PROFESSIONAL PROOFREADING</div>
    <div class="title__services">SERVICES</div>
  </header>
  <section class="details">
    <h3 class="details__heading"><svg><use href="#icon-tick"/></svg>Professional, English-language proofreading:</h3>
    <ul class="details__list">
      <li>Help with English as a second language (ESL - native English speaker with English Honours degree will correct all English language errors, spelling and grammar mistakes.</li>
      <li>Includes referencing and editing for style, coherence and clarity</li>
      <li>Fast, negotiable time-frames.</li>
    </ul>
    <h3 class="details__heading"><svg><use href="#icon-tick"/></svg>Types of proof-read documents:</h3>
    <ul class="details__list details__list--docs">
      <li>Essays / Assignments / Theses / Resumes</li>
      <li>Business Correspondence / Training Manuals / Newsletters</li>
      <li>Advertising Copy / Brochures / Catalogues / Media Releases</li>
      <li>Websites / Presentations / Speeches</li>
      <li>Novels / Short Stories</li>
    </ul>
    <h3 class="details__heading"><svg><use href="#icon-tick"/></svg>Price guide:</h3>
    <ul class="details__list">
      <li>Prices starting at $20 per page. Additional charges may apply for longer and/or more complex documents (e.g. documents requiring specialist help with English as a second language).</li>
      <li>Discounts for not-for-profit organisations and students. Special student discount rate: $25 per hour - roughly 1000 words (4 pages) of well-written text.</li>
      <li>Package deals on documents over 50,000 words.</li>
      <li>Fast turnaround times (same day service can be provided by special arrangement).</li>
    </ul>
  </section>
  <section class="testimonial">
    <h3 class="testimonial__label">Testimonial:</h3>
    <p class="testimonial__quote"><span class="mark mark--open">“</span>Hannah understood our requirements quickly and has been fantastic at delivering quality work, on time and within agreed budget. It's a pleasure to work with her. <span class="mark">”</span></p>
    <div class="testimonial__author">
      <div class="testimonial__name">Carol Ashby</div>
      <div class="testimonial__role">Operations Manager<br>Brightwell AU</div>
    </div>
  </section>
  <div class="website">www.vellumcheck.com.au</div>
  <section class="contact">
    <div class="contact__cta">Contact us for an obligation-free quote:</div>
    <div class="contact__phone">0491 570 156</div>
    <div class="contact__email"><svg><use href="#icon-mail"/></svg>proofing@vellumcheck.com.au</div>
  </section>
</article>

<!-- A6 flyer -->
<article class="flyer flyer--a6">
  <svg class="flyer__shapes" viewBox="0 0 475 672" aria-hidden="true">
    <polygon points="0,0 475,0 475,127 0,282" fill="var(--teal)"/>
    <polygon points="0,282 105,248 212,672 0,672" fill="var(--slate)"/>
    <circle cx="390" cy="32" r="95" fill="var(--ink)"/>
  </svg>
  <div class="brand-mark">VellumCheck</div>
  <header class="title">
    <div class="title__name">VELLUMCHECK</div>
    <div class="title__tagline">PROFESSIONAL PROOFREADING</div>
    <div class="title__services">SERVICES</div>
  </header>
  <section class="details">
    <h3 class="details__heading"><svg><use href="#icon-tick"/></svg>Professional, English-language proofreading:</h3>
    <ul class="details__list">
      <li>Help with English as a second language (ESL - native English speaker with English Honours degree will correct all English language errors, spelling and grammar mistakes.</li>
      <li>Includes referencing and editing for style, coherence and clarity</li>
      <li>Fast, negotiable time-frames.</li>
    </ul>
    <h3 class="details__heading"><svg><use href="#icon-tick"/></svg>Types of proof-read documents:</h3>
    <ul class="details__list details__list--docs">
      <li>Essays / Assignments / Theses / Resumes</li>
      <li>Business Correspondence / Training Manuals / Newsletters</li>
      <li>Advertising Copy / Brochures / Catalogues / Media Releases</li>
      <li>Websites / Presentations / Speeches</li>
      <li>Novels / Short Stories</li>
    </ul>
    <h3 class="details__heading"><svg><use href="#icon-tick"/></svg>Price guide:</h3>
    <ul class="details__list">
      <li>Prices starting at $20 per page. Additional charges may apply for longer and/or more complex documents (e.g. documents requiring specialist help with English as a second language).</li>
      <li>Discounts for not-for-profit organisations and students. Special student discount rate: $25 per hour - roughly 1000 words (4 pages) of well-written text.</li>
      <li>Package deals on documents over 50,000 words.</li>
      <li>Fast turnaround times (same day service can be provided by special arrangement).</li>
    </ul>
  </section>
  <section class="testimonial">
    <h3 class="testimonial__label">Testimonial:</h3>
    <p class="testimonial__quote"><span class="mark mark--open">“</span>Hannah understood our requirements quickly and has been fantastic at delivering quality work, on time and within agreed budget. It's a pleasure to work with her. <span class="mark">”</span></p>
    <div class="testimonial__author">
      <div class="testimonial__name">Carol Ashby</div>
      <div class="testimonial__role">Operations Manager<br>Brightwell AU</div>
    </div>
  </section>
  <div class="website">www.vellumcheck.com.au</div>
  <section class="contact">
    <div class="contact__cta">Contact us for an obligation-free quote:</div>
    <div class="contact__phone">0491 570 156</div>
    <div class="contact__email"><svg><use href="#icon-mail"/></svg>proofing@vellumcheck.com.au</div>
  </section>
</article>

<div class="size-label size-label--a4">A4</div>
<div class="size-label size-label--a6">A6</div>

</body>
</html>
```